2 Funky Pages + EASY stock logo = Construction Website

We would like a funky new website - Just 2 pages - to promote our project management company. A logo is also needed, but we'll provide a stock image which just needs a colour change a text added.

Here are the instructions:

"Fair Tally Homes"

#logo
The one I'd like is attached. Please change font and positioning of text though.

Tagline is "Don't be normal - Be clever"

#Colour combo
756897 Wood Veneer
D5D6D2 sand dollar
353C3F charcoal
962715 brick red

#Home - Page 1

Our cost-price home build service will save you thousands.
No, seriously - Here's how we do it (button)

- Pay what the home building companies do.
- FTH will manage the entire project.
- Use Keystonecraft Guaranteed builders and materials.
- Tender for the best industry rates.
- Get a full budget calculated for the build.
- Avoid inflated 'Fixed-price' builds.
See how it works (button)

Contact Us: 0800 615 278
enquire - Name, Phone, email, comment - SEND

#How it works - Page 2

Traditional fixed price contracts are popular because it means that any risk of unexpected problems is carried by the home builder, but the builder will generally load the price about 10 times above the actual risk carried.

It's like an over-priced insurance policy, on steroids.

Clever people do things differently.

Here's how a cost-price build works...

1) Tell us what you want to build. Dream home, townhouse, investment property, whatever.

2) We'll put a design together for you, or you can choose from a bunch of plans we've already got.

3) We'll give you a conservative price estimate.

4) We finish tweaking your plans, then send them out to our network of more than 200 builders, subcontractors and tradesmen.

5) We collect the quotes, pick the best prices, and finalise your budget. Now you buy us beer, cause you've finally realised how much you're saving.

6) Tell your friends how awesome we are, while we lodge your building consent application with Council.

7) We coordinate the builders and subbies (look, you're already speaking trade-talk) from start to finish. You pay the cost price on their work each month.

We're happy to talk numbers and give you an estimate.

Contact Us: 0800 615 278

Reason: I have seen some great design elements, but need them to come together in one site design. Also, there appears to be less attention paid to the second page design ('how it works') than is necessary... There is no viable contender there yet, compared with the great home page submissions. I've also added some further info to the brief, and note that many submissions have ignored the colour combo I've requested.

Industry/Entity Type

Construction

Number of Pages Required

2 page

Requirements
Must have
• Keystonecrafter logo (small)
• Colour combo described in brief.
Nice to have
• I've attached a stock image I like, but it's certainly not essential. I do like images with clear backgrounds though - they tend to produce a crisp looking site.
• There is a wider image similar to this, available on Pixel Vault, but Sketch Hive won't let me attach it.
Should not have
• Photos of cheesy American faces.

```html
<!DOCTYPE html>
<html lang="en">
<head>
<meta charset="utf-8">
<title>Fair Tally Homes — How it works</title>
<link rel="stylesheet" href="https://fonts.googleapis.com/css2?family=Bebas+Neue&family=Fjalla+One&family=Permanent+Marker&family=Open+Sans:wght@400&display=swap">
<style>
  :root {
    --sand-dollar: #d5d6d2;
    --charcoal: #2c3236;
    --charcoal-footer: #353c3f;
    --brick-red: #962715;
    --wood-veneer: #756897;
    --ochre: #9b6630;
    --dusty-rose: #9a6564;
    --tan: #d09a66;
    --olive: #9a9a66;
    --form-grey: #a7a9a1;
    --ink: #333638;
    --white: #ffffff;
    --num-gold: #f5c044;
    --num-pink: #f9c2c2;
    --num-cream: #fdf0b0;
  }
  * { box-sizing: border-box; margin: 0; padding: 0; }
  html, body { width: 1085px; height: 1200px; overflow: hidden; }
  body {
    position: relative;
    background: var(--sand-dollar);
    font-family: "Bebas Neue", "Fjalla One", sans-serif;
    color: var(--white);
  }

  /* Header */
  .site-header { position: absolute; left: 0; top: 0; width: 1085px; height: 212px; }
  .brand {
    position: absolute; left: 0; right: 0; top: 66px;
    display: flex; justify-content: center; align-items: center; gap: 12px;
  }
  .brand-mark { width: 22px; height: 22px; background: var(--brick-red); }
  .brand-name { font-size: 44px; color: var(--brick-red); letter-spacing: 1px; line-height: 1; }
  .tagline {
    position: absolute; left: 0; right: 0; top: 176px;
    text-align: center; font-size: 24px; letter-spacing: 1px; color: var(--ink);
  }
  .tagline::after {
    content: ""; display: block; width: 220px; height: 1px; margin: 2px auto 0;
    background: #b9bab6;
  }

  .rule { position: absolute; left: 0; width: 1085px; height: 2px; background: var(--white); }

  /* Hero */
  .hero {
    position: absolute; left: 0; top: 214px; width: 1085px; height: 184px;
    background: linear-gradient(100deg, #8a6048 0%, #a87a5a 30%, #9c7a68 55%, #b08058 75%, #7a6448 100%);
  }
  .hero-text {
    position: absolute; left: 0; right: 0; top: 30px;
    text-align: center; font-size: 24px; line-height: 34px; letter-spacing: 1px;
    text-shadow: 0 1px 2px rgba(0,0,0,.35);
  }
  .hero-text .big { font-size: 33px; }

  /* Intro band */
  .intro {
    position: absolute; left: 0; top: 400px; width: 1085px; height: 113px;
    background: var(--charcoal);
    text-align: center; font-size: 19px; line-height: 28.5px; letter-spacing: 1px;
    padding-top: 16px;
  }

  /* Steps grid */
  .steps {
    position: absolute; left: 98px; top: 517px; width: 887px;
    display: grid; grid-template-columns: 295px 296px 296px;
    grid-template-rows: 119px 122px 123px;
  }
  .step {
    position: relative; display: flex; align-items: center; justify-content: center;
    text-align: center; font-size: 16px; line-height: 23px; letter-spacing: .5px;
    text-shadow: 1px 1px 1px rgba(0,0,0,.4);
    padding: 0 6px;
  }
  .step .big { font-size: 24px; }
  .step .mid { font-size: 19px; }
  .step-num {
    position: absolute; left: 6px; top: 4px;
    font-family: "Permanent Marker", cursive; font-size: 42px; line-height: 1;
    text-shadow: none;
  }
  .step--ochre { background: var(--ochre); }
  .step--rose { background: var(--dusty-rose); }
  .step--tan { background: var(--tan); }
  .step--olive { background: var(--olive); }
  .step--wide { grid-column: 1 / 4; }
  .num-gold { color: var(--num-gold); }
  .num-pink { color: var(--num-pink); }
  .num-cream { color: var(--num-cream); }
  .step--wide .step-num { position: static; font-size: 46px; margin-right: 8px; align-self: flex-start; margin-top: 14px; }
  .step--wide .step-body { margin-left: -40px; }

  /* Enquiry */
  .enquiry {
    position: absolute; left: 0; top: 881px; width: 1085px; height: 277px;
    background: var(--form-grey);
  }
  .enquiry-form { position: absolute; left: 361px; top: 11px; width: 330px; }
  .field {
    display: block; width: 330px; height: 25px; margin-bottom: 13px;
    border: 1px solid #8e908a; background: var(--white);
    font-family: "Open Sans", sans-serif; font-size: 11px; color: #666;
    padding: 0 8px;
  }
  .field--comment { height: 91px; padding-top: 6px; resize: none; }
  .send {
    position: absolute; left: 59px; top: 228px; width: 209px; height: 40px;
    background: var(--wood-veneer); border: 2px solid var(--white); border-radius: 2px;
    color: var(--white); font-family: "Bebas Neue", sans-serif; font-size: 18px; letter-spacing: 2px;
  }
  .enquiry-note {
    position: absolute; left: 686px; top: 69px; width: 300px;
    text-align: center; color: var(--ink); font-size: 25px; line-height: 34px; letter-spacing: 1.5px;
  }
  .enquiry-note .phone { display: block; font-size: 32px; margin-top: 2px; }

  /* Footer */
  .site-footer {
    position: absolute; left: 0; top: 1158px; width: 1085px; height: 42px;
    background: var(--charcoal-footer);
    text-align: center; line-height: 42px;
    font-family: "Open Sans", sans-serif; font-size: 11px; letter-spacing: .5px; color: #e6e6e6;
  }
</style>
</head>
<body>

<header class="site-header">
  <div class="brand">
    <span class="brand-mark"></span>
    <span class="brand-name">Fair Tally Homes</span>
  </div>
  <p class="tagline">Don't be normal - be clever</p>
</header>

<div class="rule" style="top:212px"></div>

<section class="hero" role="img" aria-label="Soft-focus photograph of a timber family home">
  <p class="hero-text">
    Traditional <span class="big">fixed price</span> contracts are popular<br>
    because it means that any <span class="big">risk</span> of <span class="big">unexpected problems</span><br>
    is carried by the home builder, but the builder will generally<br>
    <span class="big">load</span> the price about <span class="big">10 times above</span> the actual risk carried.
  </p>
</section>

<div class="rule" style="top:398px"></div>

<section class="intro">
  It's like an over-priced insurance policy,<br>
  on steroids. Clever people do things differently.<br>
  Here's how a cost-price build works...
</section>

<div class="rule" style="top:514px"></div>

<section class="steps">
  <div class="step step--ochre">
    <span class="step-num num-gold">1</span>
    <p>Tell us what you want to build.<br><span class="mid">Dream home,</span> <span class="big">townhouse,</span><br><span class="mid">investment property,</span> whatever.</p>
  </div>
  <div class="step step--rose">
    <span class="step-num num-pink">2</span>
    <p><span class="mid">We'll put a design</span><br>together for you,<br>or you can choose from<br>a bunch of plans we've already got.</p>
  </div>
  <div class="step step--ochre">
    <span class="step-num num-gold">3</span>
    <p>We'll give you<br><span class="big">a conservative</span><br><span class="mid">price estimate.</span></p>
  </div>
  <div class="step step--tan">
    <span class="step-num num-cream">4</span>
    <p>We finish <span class="mid">tweaking</span> your plans,<br><span class="mid">then send them out to our network</span><br><span class="mid">of more than 200 builders,</span><br><span class="mid">subcontractors and tradesmen.</span></p>
  </div>
  <div class="step step--ochre">
    <span class="step-num num-gold">5</span>
    <p><span class="mid">We collect the quotes, pick</span><br><span class="mid">the best prices, and finalise</span><br><span class="mid">your budget.</span> Now you buy us beer,<br><span class="mid">cause you've finally realised</span><br>how much you're saving.</p>
  </div>
  <div class="step step--olive">
    <span class="step-num num-cream">6</span>
    <p>Tell your friends<br><span class="mid">how awesome we are,</span><br>while we lodge your building consent<br>application with Council.</p>
  </div>
  <div class="step step--rose step--wide">
    <span class="step-num num-pink">7</span>
    <p class="step-body"><span class="mid">We coordinate the builders and subbies</span><br>(look, you're already speaking trade-talk)<br><span class="mid">from start to finish. You pay the cost price on their work each month.</span></p>
  </div>
</section>

<section class="enquiry">
  <form class="enquiry-form">
    <input class="field" type="text" placeholder="NAME">
    <input class="field" type="tel" placeholder="PHONE">
    <input class="field" type="email" placeholder="EMAIL">
    <textarea class="field field--comment" placeholder="COMMENT"></textarea>
    <button class="send" type="button">Send</button>
  </form>
  <p class="enquiry-note">
    We're happy<br>to talk numbers<br>and give you an estimate.
    <span class="phone">0800 615 278</span>
  </p>
</section>

<footer class="site-footer">FAIR TALLY HOMES © 2016</footer>

</body>
</html>
```